Freelance Makeup Artist Needing Business Card Design

I am a freelance makeup artist looking for a design for my business cards.
My target audience is people looking for bridal makeup, so i was thinking minimalistic style, black with white or gold foil accents.
Something that feels classy but simple and to the point.

I would like the front to state Marisa Pelworth and Makeup Artist, and the back to include my social media and contact details.

Target Market(s)

Brides, young women

Industry/Entity Type

Business

Contact Information for Business Card

0417352840
marisa.pelworth@quorvel.com
www.snapvale.com/marisa.pelworth
www.friendloop.com/MarisaPelworthMakeup

Requirements
Nice to have
• Social media icons next to relevant contact details

```html
<!DOCTYPE html>
<html lang="en">
<head>
<meta charset="utf-8">
<title>Marisa Pelworth – Makeup Artist Business Card</title>
<link rel="stylesheet" href="https://fonts.googleapis.com/css2?family=Montserrat:wght@400;700&family=Didact+Gothic&display=swap">
<style>
  :root {
    --page-bg: #e6e6e8;
    --card-black: #0c0c0c;
    --card-black-top: #2b2b2b;
    --band-light: #e4e4e2;
    --band-grey: #4f5052;
    --ink-white: #f4f4f4;
    --ink-silver: #c9c9c9;
    --ink-muted: #9c9c9c;
    --ink-dark: #1a1a1a;
  }
  * { box-sizing: border-box; margin: 0; padding: 0; }
  html, body { width: 1200px; height: 881px; overflow: hidden; }
  body {
    background: var(--page-bg);
    display: flex;
    flex-direction: column;
    align-items: center;
    justify-content: center;
    gap: 52px;
  }
  .card {
    width: 620px;
    height: 354px;
    position: relative;
    overflow: hidden;
    box-shadow: 0 10px 30px rgba(0,0,0,.25);
  }

  /* Front */
  .card-front {
    background: linear-gradient(160deg, var(--card-black-top) 0%, var(--card-black) 60%, #050505 100%);
  }
  .front-identity {
    position: absolute;
    left: 150px;
    top: 132px;
  }
  .front-name {
    font-family: "Montserrat", sans-serif;
    font-weight: 700;
    font-size: 38px;
    letter-spacing: .5px;
    color: var(--ink-white);
    line-height: 1;
  }
  .front-title {
    font-family: "Montserrat", sans-serif;
    font-weight: 400;
    font-size: 18px;
    color: var(--ink-muted);
    margin: 8px 0 0 40px;
  }

  /* Back */
  .card-back { background: var(--card-black); }
  .back-top-band {
    position: absolute; left: 0; top: 0; right: 0; height: 112px;
    background: var(--band-light);
  }
  .back-name {
    position: absolute; left: 148px; top: 116px;
    font-family: "Montserrat", sans-serif;
    font-weight: 700; font-size: 30px; color: var(--ink-dark);
    background: var(--band-light);
    padding: 0 8px 2px 6px;
    top: 86px;
    line-height: 1.1;
  }
  .back-title {
    position: absolute; left: 150px; top: 126px;
    font-family: "Montserrat", sans-serif;
    font-size: 14px; color: var(--ink-silver);
  }
  .contact-list {
    position: absolute; right: 22px; top: 190px;
    list-style: none;
    font-family: "Didact Gothic", sans-serif;
    font-variant: small-caps;
    font-size: 13px;
    color: var(--ink-white);
    text-align: right;
  }
  .contact-list li {
    display: flex; align-items: center; justify-content: flex-end;
    gap: 10px; margin-bottom: 12px;
  }
  .icon-dot {
    width: 14px; height: 14px; border-radius: 50%;
    background: var(--ink-white); flex: none;
  }
  .contact-email { margin-top: 14px; }
  .icon-ring {
    width: 16px; height: 16px; flex: none;
  }
  .back-bottom-strip {
    position: absolute; left: 0; right: 0; bottom: 0; height: 42px;
    background: var(--band-grey);
    display: flex; align-items: center; padding-left: 22px; gap: 12px;
    font-family: "Didact Gothic", sans-serif;
    font-size: 14px; letter-spacing: 3px; color: var(--ink-white);
  }
</style>
</head>
<body>

  <section class="card card-front" aria-label="Business card front">
    <div class="front-identity">
      <h1 class="front-name">Marisa Pelworth</h1>
      <p class="front-title">Makeup Artist</p>
    </div>
  </section>

  <section class="card card-back" aria-label="Business card back">
    <div class="back-top-band"></div>
    <h2 class="back-name">Marisa Pelworth</h2>
    <p class="back-title">Makeup Artist</p>

    <ul class="contact-list">
      <li>www.snapvale.com/marisa.pelworth <span class="icon-dot"></span></li>
      <li>www.friendloop.com/MarisaPelworthMakeup <span class="icon-dot"></span></li>
      <li class="contact-email">marisa.pelworth@quorvel.com
        <svg class="icon-ring" viewBox="0 0 16 16" aria-hidden="true">
          <circle cx="8" cy="8" r="7" fill="none" stroke="#f4f4f4" stroke-width="1.2"/>
          <rect x="4" y="5.5" width="8" height="5" fill="none" stroke="#f4f4f4" stroke-width="1"/>
          <polyline points="4,5.5 8,8.5 12,5.5" fill="none" stroke="#f4f4f4" stroke-width="1"/>
        </svg>
      </li>
    </ul>

    <div class="back-bottom-strip">
      <svg class="icon-ring" viewBox="0 0 16 16" aria-hidden="true">
        <circle cx="8" cy="8" r="7" fill="none" stroke="#f4f4f4" stroke-width="1.2"/>
        <path d="M5.5 4.5 L7 4.5 L7.6 6.4 L6.7 7.1 Q7.5 8.7 9 9.4 L9.7 8.5 L11.5 9.1 L11.5 10.6 Q8.5 11.2 6.3 8.9 Q4.6 7 5.5 4.5 Z" fill="#f4f4f4"/>
      </svg>
      <span class="phone">0417352840</span>
    </div>
  </section>

</body>
</html>
```